Business Cards

Now that we have a fantastic logo, we need business cards designed for our organization.
We'd like a design that uses our logo and is very creative and eye catching. It should have the following copy, in addition to our logo. It can be standard business card size, or smaller.
Cultivate. Connect. Create.
1128 Pelham Avenue
Willits, California
Mendocino County
California
United States of America
url: www.larkspurrowguild.org
twitter: #larkspurcraft
facebook, linkedin, google+, and tumblr: larkspur row guild
email: info@larkspurrowguild

```html
<!DOCTYPE html>
<html lang="en">
<head>
<meta charset="utf-8">
<title>Larkspur Row Guild — Business Card</title>
<link rel="stylesheet" href="https://fonts.googleapis.com/css2?family=Alegreya:wght@400&family=Marcellus&family=Raleway:wght@300&display=swap">
<style>
  :root {
    --paper: #ffffff;
    --pumpkin: #ea7f2c;
    --sage: #98a65f;
    --leaf-red: #e4502a;
    --leaf-gold: #f2b62a;
    --band: #4c4b45;
    --peach: #f3b581;
    --ink: #5a5a58;
    --address: #ffffff;
  }
  html, body {
    margin: 0;
    padding: 0;
    overflow: hidden;
    background: var(--paper);
  }
  .card {
    position: relative;
    width: 1200px;
    height: 686px;
    overflow: hidden;
    background: var(--paper);
  }
  .card__backdrop {
    position: absolute;
    inset: 0;
  }
  .card__leaves {
    position: absolute;
    left: 400px;
    top: 0;
    width: 800px;
    height: 686px;
    background:
      radial-gradient(circle at 15% 20%, rgba(234,127,44,0.55), transparent 22%),
      radial-gradient(circle at 30% 55%, rgba(228,80,42,0.45), transparent 20%),
      radial-gradient(circle at 70% 10%, rgba(242,182,42,0.5), transparent 18%),
      radial-gradient(circle at 85% 45%, rgba(228,80,42,0.45), transparent 20%),
      radial-gradient(circle at 80% 88%, rgba(242,182,42,0.55), transparent 22%),
      radial-gradient(circle at 20% 92%, rgba(234,127,44,0.6), transparent 14%);
  }
  .card__address {
    position: absolute;
    right: 29px;
    top: 78px;
    margin: 0;
    font-family: "Alegreya", serif;
    font-size: 42px;
    line-height: 67px;
    color: var(--address);
    text-align: right;
    text-shadow: 1px 2px 2px rgba(40,40,30,0.85);
    font-style: normal;
  }
  .card__motto {
    position: absolute;
    left: 0;
    top: 443px;
    width: 1200px;
    height: 90px;
    background: var(--band);
    display: flex;
    align-items: center;
    justify-content: space-between;
    padding: 0 34px;
    box-sizing: border-box;
    font-family: "Marcellus", serif;
    font-size: 52px;
    letter-spacing: 1px;
    color: var(--peach);
  }
  .card__name {
    position: absolute;
    left: 30px;
    top: 548px;
    margin: 0;
    font-family: "Raleway", sans-serif;
    font-weight: 300;
    font-size: 56px;
    line-height: 60px;
    color: var(--ink);
  }
</style>
</head>
<body>
  <div class="card">
    <svg class="card__backdrop" width="1200" height="686" viewBox="0 0 1200 686" aria-hidden="true">
      <circle cx="869" cy="343" r="446" fill="var(--sage)"/>
      <rect x="0" y="0" width="445" height="533" fill="var(--pumpkin)"/>
    </svg>
    <div class="card__leaves" role="img" aria-label="Scattered autumn maple leaves in red, orange and gold"></div>

    <address class="card__address">
      1128 Pelham Avenue<br>
      Willits, California<br>
      Mendocino County<br>
      California<br>
      United States of America
    </address>

    <div class="card__motto">
      <span>CULTIVATE.</span>
      <span>CONNECT.</span>
      <span>CREATE.</span>
    </div>

    <p class="card__name">larkspur row<br>guild</p>
  </div>
</body>
</html>
```